New Business Card Design Project VORASTI-Italy

we are VORASTI-Italy
our company in the market for 3 years we are luxury cosmetic company and its about time for a facelift :)
i will like to have elegant luxurious and unique business card
that will give the person that get it a unique, luxurious and elegant impression
I'm VERY OPEN FOR NEW IDEAS , even duo i add a few files of things that i see on line and i like them

i add my logo as well
my website is VORASTI.COM
(if you would like to see the main style that we have)

Target Market(s)

adult that have money :)

Industry/Entity Type

Business

Contact Information for Business Card

Name - Paul Vorasti
Position - CEO and CO Founder
address - 4817 E Larkdale
telephone - 555-384-1962
email - paul@vorasti.com
fax - 555-384-1962
website - VORASTI.COM

Colors
000000
959595
fbee3e
ffffff

Requirements
Must have
• big logo in GOLD color
• elegant look
• impressive
Nice to have
• not must but maybe classy pattern background
• not must but maybe emblem
• maybe clear plastic business card
Should not have
• colors
• images

```html
<!DOCTYPE html>
<html lang="en">
<head>
<meta charset="utf-8">
<title>VORASTI Italy – Business Card</title>
<link rel="stylesheet" href="https://fonts.googleapis.com/css2?family=Cormorant+Garamond:wght@500;600&family=Playfair+Display:wght@700&family=Arimo:wght@400&display=swap">
<style>
  :root {
    --stage: #1c1c1c;
    --card-top: #4b382d;
    --card-bottom: #2b2320;
    --gold: #e9c34a;
    --gold-light: #fbee3e;
    --gold-deep: #b98d22;
    --ink-light: #ffffff;
    --ink-muted: #d9d4cf;
  }
  * { box-sizing: border-box; }
  html, body {
    margin: 0;
    width: 1200px;
    height: 900px;
    overflow: hidden;
    background: var(--stage);
  }
  .canvas {
    position: relative;
    width: 1200px;
    height: 900px;
  }
  .card {
    position: absolute;
    top: 160px;
    width: 340px;
    height: 580px;
    border-radius: 26px;
    overflow: hidden;
    background: linear-gradient(160deg, var(--card-top) 0%, var(--card-bottom) 75%);
    box-shadow: 0 18px 40px rgba(0,0,0,.55);
  }
  .card--front { left: 240px; }
  .card--back  { left: 620px; }

  /* Front */
  .front-brand {
    position: absolute;
    top: 48px;
    left: 0;
    right: 0;
    text-align: center;
    color: var(--gold);
  }
  .front-brand__name {
    font-family: "Cormorant Garamond", serif;
    font-weight: 600;
    font-size: 46px;
    letter-spacing: 1px;
    line-height: 1;
    margin: 0;
  }
  .front-brand__rule {
    width: 190px;
    height: 2px;
    margin: 6px auto 0;
    background: var(--gold);
  }
  .front-brand__place {
    font-family: "Cormorant Garamond", serif;
    font-weight: 600;
    font-size: 15px;
    letter-spacing: 2px;
    margin-top: 4px;
  }
  .front-emblem-area {
    position: absolute;
    left: -20px;
    top: 175px;
    width: 440px;
    height: 440px;
    border-radius: 50%;
    background: radial-gradient(circle at 45% 45%, rgba(43,35,32,1) 0 34%, var(--gold-deep) 36%, var(--gold) 55%, var(--gold-light) 70%, var(--gold) 100%);
  }

  /* Back */
  .back-mark {
    position: absolute;
    top: 46px;
    left: 50%;
    transform: translateX(-50%);
    width: 96px;
    height: 96px;
    border-radius: 50%;
    background: var(--gold);
  }
  .back-mark__name {
    position: absolute;
    top: 152px;
    left: 0;
    right: 0;
    text-align: center;
    font-family: "Cormorant Garamond", serif;
    font-weight: 600;
    font-size: 18px;
    letter-spacing: 3px;
    color: var(--gold);
  }
  .person {
    position: absolute;
    top: 196px;
    left: 0;
    right: 0;
    text-align: center;
  }
  .person__name {
    margin: 0;
    font-family: "Playfair Display", serif;
    font-weight: 700;
    font-size: 32px;
    color: var(--gold);
    line-height: 1.1;
  }
  .person__role {
    margin-top: 4px;
    font-family: "Arimo", sans-serif;
    font-size: 13px;
    color: var(--ink-light);
  }
  .contact-list {
    position: absolute;
    top: 305px;
    left: 78px;
    margin: 0;
    padding: 0;
    list-style: none;
    font-family: "Arimo", sans-serif;
    font-size: 14px;
    color: var(--ink-light);
  }
  .contact-list__item {
    display: flex;
    align-items: flex-start;
    gap: 12px;
    margin-bottom: 16px;
    line-height: 1.25;
  }
  .contact-list__icon {
    width: 14px;
    height: 14px;
    flex: none;
    margin-top: 1px;
    fill: var(--gold);
  }
</style>
</head>
<body>
<main class="canvas">

  <section class="card card--front" aria-label="Business card front">
    <div class="front-brand">
      <h1 class="front-brand__name">VORASTI</h1>
      <div class="front-brand__rule"></div>
      <div class="front-brand__place">ITALY</div>
    </div>
    <div class="front-emblem-area" role="img" aria-label="Large gold ornamental emblem"></div>
  </section>

  <section class="card card--back" aria-label="Business card back">
    <div class="back-mark"></div>
    <div class="back-mark__name">VORASTI</div>

    <div class="person">
      <h2 class="person__name">Paul Vorasti</h2>
      <div class="person__role">CEO and CO Founder</div>
    </div>

    <ul class="contact-list">
      <li class="contact-list__item">
        <svg class="contact-list__icon" viewBox="0 0 16 16"><path d="M15 1 1 7l6 2 2 6z"/></svg>
        <span>4817 E Larkdale<br>Silver Bend Nevada 89140</span>
      </li>
      <li class="contact-list__item">
        <svg class="contact-list__icon" viewBox="0 0 16 16"><path d="M3 1h3l1 4-2 1c1 2 3 4 5 5l1-2 4 1v3c0 1-1 2-2 2C7 15 1 9 1 3c0-1 1-2 2-2z"/></svg>
        <span>555-384-1962</span>
      </li>
      <li class="contact-list__item">
        <svg class="contact-list__icon" viewBox="0 0 16 16"><path d="M1 3h14v1L8 9 1 4z"/><path d="M1 6l7 5 7-5v7H1z"/></svg>
        <span>paul@vorasti.com</span>
      </li>
      <li class="contact-list__item">
        <svg class="contact-list__icon" viewBox="0 0 16 16"><path d="M4 1h6l2 2v3H4z"/><path d="M2 7h12v8H2zm3 2v2h2V9zm4 0v2h2V9z"/></svg>
        <span>555-384-1962</span>
      </li>
      <li class="contact-list__item">
        <svg class="contact-list__icon" viewBox="0 0 16 16"><path d="M8 1a7 7 0 1 0 0 14A7 7 0 0 0 8 1zm0 1.5c.8 0 1.7 1.7 2 4.5H6c.3-2.8 1.2-4.5 2-4.5zM2.6 7h2c.1-1.7.4-3 .9-4A5.5 5.5 0 0 0 2.6 7zm8.8 0h2a5.5 5.5 0 0 0-2.9-4c.5 1 .8 2.3.9 4zM2.6 9a5.5 5.5 0 0 0 2.9 4c-.5-1-.8-2.3-.9-4zm3.4 0c.3 2.8 1.2 4.5 2 4.5s1.7-1.7 2-4.5zm5.4 0c-.1 1.7-.4 3-.9 4a5.5 5.5 0 0 0 2.9-4z"/></svg>
        <span>www.vorasti.com</span>
      </li>
    </ul>
  </section>

</main>
</body>
</html>
```